User help guide for software for investment bank

We need a professional design for our user help guides for new software we have written for our client. We develop visualization software for investment banks in Singapore mainly focused in the financial and risk management area. Our help guides are design to show them how the software works as well as promote our brand
Updates

Target Market(s)

Investment banking, risk management, finance

Industry/Entity Type

Bank

Requirements
Must have
• Content of document and logos
• Colour sheme
• Professional brouchure design
• Verindo and plunox logos on it
• Look at www.verindo-example.com for company looks and feel
• PLEASE USE COLOUR SCHEMES BELOW IN ATTACHMENT AND FOLLOW SIMILAR STYLE TO CLIENT ANNUAL REPORT

```html
<!DOCTYPE html>
<html lang="en">
<head>
<meta charset="utf-8">
<title>Web Editing Tool – User Guide Covers</title>
<link rel="stylesheet" href="https://fonts.googleapis.com/css2?family=Inter:wght@300;400;500&display=swap">
<style>
  :root {
    --backdrop: #e6e3df;
    --ink: #1a1a1a;
    --page-black: #050505;
    --paper: #ffffff;
    --brand-red: #e41e26;
    --cyan: #1aaee6;
    --cyan-mid: #62c9ef;
    --cyan-pale: #dff1fa;
    --label-text: #0b3a55;
    --logo-text: #ffffff;
    --client-text: #2a3b5c;
    --machine-dark: #1b1d20;
    --machine-mid: #3a3f46;
    --machine-light: #7d858e;
  }
  * { box-sizing: border-box; margin: 0; padding: 0; }
  html, body {
    width: 1200px; height: 1000px; overflow: hidden;
    background: var(--backdrop);
    font-family: "Inter", "Helvetica Neue", Arial, sans-serif;
    color: var(--ink);
  }
  .spread { position: relative; width: 1200px; height: 1000px; }
  .page {
    position: absolute; top: 130px; width: 510px; height: 720px;
    overflow: hidden; background: var(--page-black);
    box-shadow: 0 10px 30px rgba(0,0,0,.25);
  }
  .page--front { left: 60px; }
  .page--back { left: 630px; }

  .artwork {
    position: absolute; left: 20px; top: 40px; width: 470px; height: 270px;
    background: radial-gradient(ellipse at 50% 50%, var(--machine-light) 0%, var(--machine-mid) 35%, var(--machine-dark) 65%, var(--page-black) 100%);
    opacity: .9;
  }

  .red-band { position: absolute; background: var(--brand-red); }
  .page--front .red-band { left: 160px; right: 0; top: 330px; height: 52px; }
  .page--back .red-band { left: 160px; right: 0; top: 642px; height: 48px; }
  .page--back .red-rule { position: absolute; left: 110px; width: 50px; top: 642px; height: 2px; background: var(--brand-red); }

  .partner-name {
    position: absolute;
    font-size: 14px; font-weight: 400; letter-spacing: 2px; line-height: 1; color: var(--logo-text);
  }
  .page--front .partner-name { left: 40px; top: 358px; }
  .page--back .partner-name { left: 40px; top: 664px; }

  .cover-body {
    position: absolute; left: 0; right: 0; top: 392px; bottom: 0;
    background: var(--paper); padding: 0 40px;
  }
  .doc-title {
    margin-top: 55px; font-size: 40px; font-weight: 300; letter-spacing: -1px; color: var(--ink);
  }
  .record-caption {
    margin-top: 58px; font-size: 8px; font-weight: 400; letter-spacing: .3px; color: #333;
  }
  .record { margin-top: 5px; width: 400px; border-collapse: collapse; font-size: 8px; }
  .record td { padding: 2px 6px; height: 13px; border-right: 1px dotted rgba(255,255,255,.7); white-space: nowrap; }
  .record .label { background: var(--cyan); color: var(--label-text); width: 78px; }
  .record .value { background: var(--cyan-pale); color: #234; }
  .record .head td { background: var(--cyan-mid); color: var(--label-text); }
  .record .entry td { background: var(--cyan); color: var(--label-text); }

  .client-name {
    position: absolute; right: 42px; bottom: 44px;
    font-size: 22px; font-weight: 400; letter-spacing: 4px; line-height: 1; color: var(--client-text);
  }
</style>
</head>
<body>
<main class="spread">
  <section class="page page--front">
    <div class="artwork" role="img" aria-label="Dark illustration of interlocking gears and machine parts"></div>
    <div class="red-band"></div>
    <div class="partner-name">PLUNOX</div>
    <div class="cover-body">
      <h1 class="doc-title">Web Editing Tool</h1>
      <p class="record-caption">ISSUE / AMENDMENT RECORD</p>
      <table class="record">
        <tr><td class="label">Project ID</td><td class="value" colspan="5">QRMC – Credit Risk KLDS 15002321</td></tr>
        <tr><td class="label">Project Name</td><td class="value" colspan="5">KLDS Wholesale/ Structured Finance Templates Automation</td></tr>
        <tr><td class="label">Document Status</td><td class="value" colspan="5"></td></tr>
        <tr class="head"><td>Version</td><td>Date</td><td>Author</td><td>Reviewer</td><td>Approver</td><td>Version Summary</td></tr>
        <tr class="entry"><td>0.1</td><td>19/11/2015</td><td>Lena Dorval</td><td>Lena Dorval</td><td></td><td>Initial draft</td></tr>
      </table>
      <div class="client-name">verindo</div>
    </div>
  </section>

  <section class="page page--back">
    <div class="artwork" role="img" aria-label="Dark illustration of interlocking gears and machine parts"></div>
    <div class="red-rule"></div>
    <div class="red-band"></div>
    <div class="partner-name">PLUNOX</div>
  </section>
</main>
</body>
</html>
```